Bright Path Academy - Personal Development business 2.0 needs a social post format design.

https://www.brightpathacademy-example.com

Our focus with Bright Path Academy is on developing people through knowledge and skills to improve their everyday lives.
We love simplicity, Quince design and less is more.

We are crazy about personal growth, science, design, the latest gadgets and people.

We need 4 formats for our social media posts.
1. Blogs -to pronounce a blog post
2. Workshop /training - to pronounce our workshops/trainings (both online and offline)
3. Podcast - called "Kijk eens verder". To pronounce a guest we've spoken. The host is called Berend.
4. Facts - to pronounce short facts about personal development. Invites people to read more.
The formats should include: high quality pictogram (better than the uploaded picto's), 1 of the 3 logo's in the design.
It's important that we can edit the design in Lumora Draw / Lumora Pixel to adjust the text in the format.

Attached you find four of our current designs, which are a poor example of how the designs should look like. These are just to show you how much lines of text (more or less) will be in the designs. So please do not make a design that looks like these ;) You have carte blanche.

Our customers are mostly women (80%). We focus on both business and casual customers.

Target Market(s)

80% woman, 20% men. We focus on both business and casual customers.

Requirements
Must have
• Less is more. Quince Design alike. Simplicity.
Aimed at the women target audience.
Designs must be edible for adjusting the text in the format.
Nice to have
• Unique concept.
The design should "breathe".
Each design can have a different color, so customers identify the specific post with specific information. For example, blog is red, workshop post black, etc.

```html
<!DOCTYPE html>
<html lang="nl">
<head>
<meta charset="utf-8">
<title>Bright Path Academy – social post formats</title>
<link rel="stylesheet" href="https://fonts.googleapis.com/css2?family=Oswald:wght@300;400&family=Poppins:wght@500;600&family=Comfortaa:wght@300&family=Allura&display=swap">
<style>
  :root {
    --board: #b5a59c;
    --white: #ffffff;
    --ring: rgba(255, 255, 255, 0.55);
    --facts-sky: #2a44a0;
    --facts-dusk: #6d6a8c;
    --facts-field: #d98a2a;
    --training-deep: #1f3f95;
    --training-mid: #3f7aa3;
    --training-teal: #5db4a0;
    --blog-amber: #c06b14;
    --blog-forest: #4b3a26;
    --blog-rose: #c43f62;
  }
  * { box-sizing: border-box; margin: 0; padding: 0; }
  html, body { width: 1200px; height: 729px; overflow: hidden; }
  body { background: var(--board); position: relative; font-family: "Poppins", sans-serif; color: var(--white); }

  .post {
    position: absolute; top: 201px; width: 334px; height: 334px; overflow: hidden;
    box-shadow: 0 4px 6px rgba(0, 0, 0, 0.18);
  }
  .post--facts { left: 48px; }
  .post--training { left: 430px; }
  .post--blog { left: 811px; }

  .post__photo { position: absolute; inset: 0; }
  .post--facts .post__photo {
    background:
      linear-gradient(200deg, var(--facts-sky) 0%, rgba(80, 90, 150, 0.6) 35%, transparent 60%),
      linear-gradient(180deg, var(--facts-dusk) 0%, #b07a5c 45%, var(--facts-field) 70%, #b8752a 100%);
  }
  .post--training .post__photo {
    background:
      radial-gradient(ellipse 90px 130px at 50% 32%, rgba(160, 190, 200, 0.55), transparent 80%),
      linear-gradient(30deg, var(--training-deep) 0%, var(--training-mid) 55%, var(--training-teal) 100%);
  }
  .post--blog .post__photo {
    background:
      radial-gradient(ellipse 110px 120px at 52% 82%, rgba(235, 170, 175, 0.55), transparent 80%),
      linear-gradient(45deg, var(--blog-rose) 0%, #7a3a35 35%, var(--blog-forest) 60%, var(--blog-amber) 100%);
  }

  .brand {
    position: absolute; top: 28px; left: 21px;
    display: flex; align-items: center; gap: 6px;
    font-family: "Poppins", sans-serif; font-weight: 600; font-size: 12px; letter-spacing: 0.02em;
    color: var(--white);
  }
  .brand__dot { width: 8px; height: 8px; border-radius: 50%; background: var(--white); }

  .centered { position: absolute; left: 0; right: 0; text-align: center; }

  /* Facts */
  .facts__ring {
    position: absolute; left: 53px; top: 53px; width: 226px; height: 226px;
    border: 2px solid var(--ring); border-radius: 50%;
  }
  .facts__icon { top: 70px; }
  .facts__label { top: 107px; font-family: "Oswald", sans-serif; font-weight: 400; font-size: 14px; }
  .facts__quote { top: 118px; font-family: "Poppins", sans-serif; font-weight: 600; font-size: 72px; line-height: 1; color: rgba(255,255,255,0.45); }
  .facts__text { top: 174px; font-weight: 500; font-size: 14.5px; line-height: 18px; }

  /* Training */
  .training__icon { top: 132px; }
  .training__frame {
    position: absolute; left: 29px; top: 194px; width: 278px; height: 107px;
    border: 2px solid rgba(255,255,255,0.5); border-radius: 12px;
  }
  .training__kicker {
    top: 184px; font-family: "Oswald", sans-serif; font-weight: 400; font-size: 16px;
  }
  .training__kicker span { background: transparent; padding: 0 12px; position: relative; }
  .training__kicker span::before {
    content: ""; position: absolute; inset: 8px 0 auto 0; height: 4px;
  }
  .training__gap {
    position: absolute; left: 107px; top: 190px; width: 122px; height: 8px; background: #3a6aa4;
  }
  .training__title { top: 215px; font-family: "Oswald", sans-serif; font-weight: 400; font-size: 29px; letter-spacing: -0.01em; }
  .training__date { top: 256px; font-family: "Oswald", sans-serif; font-weight: 300; font-size: 21px; letter-spacing: -0.02em; }

  /* Blog */
  .blog__icon { top: 64px; }
  .blog__label { top: 105px; font-family: "Oswald", sans-serif; font-weight: 400; font-size: 17px; }
  .blog__title { top: 138px; font-family: "Comfortaa", sans-serif; font-weight: 300; font-size: 25px; }
  .blog__subtitle { top: 168px; font-family: "Allura", cursive; font-size: 42px; }
</style>
</head>
<body>
  <article class="post post--facts">
    <div class="post__photo" role="img" aria-label="Foto: eenzame boom in een korenveld bij zonsondergang"></div>
    <div class="brand"><span class="brand__dot"></span>Bright Path Academy</div>
    <div class="facts__ring"></div>
    <div class="centered facts__icon">
      <svg width="32" height="34" viewBox="0 0 32 34" aria-hidden="true">
        <path d="M16 2a14 14 0 1 0 6 26.7l6 3.3-1.5-6A14 14 0 0 0 16 2z" fill="none" stroke="#fff" stroke-width="2"/>
        <path d="M9 13h4l5-4v14l-5-4H9z" fill="#fff"/>
        <path d="M20.5 12.5a5 5 0 0 1 0 7M23 10a8.5 8.5 0 0 1 0 12" fill="none" stroke="#fff" stroke-width="1.6" stroke-linecap="round"/>
      </svg>
    </div>
    <div class="centered facts__label">FACTS</div>
    <div class="centered facts__quote">“</div>
    <p class="centered facts__text">Gemiddeld haalt<br>slechts 20% zijn/haar<br>goede voornemens</p>
  </article>

  <article class="post post--training">
    <div class="post__photo" role="img" aria-label="Portretfoto van de trainer met gekruiste armen"></div>
    <div class="brand"><span class="brand__dot"></span>Bright Path Academy</div>
    <div class="centered training__icon">
      <svg width="40" height="36" viewBox="0 0 40 36" aria-hidden="true">
        <rect x="2" y="1" width="36" height="24" rx="3" fill="none" stroke="#fff" stroke-width="2"/>
        <circle cx="13" cy="9" r="2.6" fill="#fff"/>
        <path d="M9 22v-7a3 3 0 0 1 3-3h3l5 4" fill="none" stroke="#fff" stroke-width="2.4" stroke-linecap="round"/>
        <path d="M20 16l9-7" stroke="#fff" stroke-width="1.2"/>
        <circle cx="8" cy="29" r="2.3" fill="#fff"/><circle cx="20" cy="29" r="2.3" fill="#fff"/><circle cx="32" cy="29" r="2.3" fill="#fff"/>
        <path d="M3 35a5 4 0 0 1 10 0zM15 35a5 4 0 0 1 10 0zM27 35a5 4 0 0 1 10 0z" fill="#fff"/>
      </svg>
    </div>
    <div class="training__frame"></div>
    <div class="training__gap" style="background:#3b6ea6"></div>
    <div class="centered training__kicker">ONLINE TRAINING</div>
    <h2 class="centered training__title">PRE-NEW YEAR’S EVE</h2>
    <p class="centered training__date">DINSDAG 29 DECEMBER, 19-21U</p>
  </article>

  <article class="post post--blog">
    <div class="post__photo" role="img" aria-label="Foto: vrouw met hoed en gespreide armen in het bos"></div>
    <div class="brand"><span class="brand__dot"></span>Bright Path Academy</div>
    <div class="centered blog__icon">
      <svg width="36" height="34" viewBox="0 0 36 34" aria-hidden="true">
        <path d="M4 2v20a9 9 0 1 0 9-9H8" fill="none" stroke="#fff" stroke-width="4.5" stroke-linecap="round"/>
        <path d="M18 6a12 12 0 0 1 11 11M18 0a18 18 0 0 1 17 17" fill="none" stroke="#fff" stroke-width="2.4" stroke-linecap="round"/>
      </svg>
    </div>
    <div class="centered blog__label">BLOG</div>
    <h2 class="centered blog__title">Goede Voornemens</h2>
    <p class="centered blog__subtitle">Die Je Volhoudt - 3 Tips</p>
  </article>
</body>
</html>
```